Brochure Design Project

Job Type:

1 unified, standard format for 4 marketing templates: doorhanger, factsheet, case study, tri-fold for an energy-services company (helping people and utilities save money)

Task Outline:

Generic templates for 4 marketing pieces that can be used-in other words: latin text fill, lots of pictures that can be replaced or modified, very professional and warm look, deliverable can be modified upon purchase for different programs since we participate in constantly changing programs (universal template is what we’re looking for). The 4 pieces should have a standard look and feel (i.e., same design, different size layout)

Task Description:

The templates will be used to inform/attract clients to our energy efficiency and renewable energy programs. These programs include home improvement measures that cut energy costs and can be funded by government rebate programs. Clients range from residential homeowners, small business owners, and mobile home owners (we will modify pictures, insert text upon delivery for each segment). The template will need to be professional and have the ability to be edited by our staff because we constantly have new programs forming.

Target Market(s)

Utilities, residential, mobile home, small commercial

Industry/Entity Type

Home Improvement

Requirements
Must have
• 1. Locations for the following logos:

VoltaCrest Ally
TPRN
KMF A+
Utility Logo
Lumora Holdings
(See example here: http://www.lumoraholdings.example/index.php?option=com_content&view=article&id=148:northbay-fuel-works-manufactured-mobile-homes&catid=44&Itemid=108)

2. Location for a utility disclaimer box (see box at the bottom of the page in the link above)

3. Location for name of program at the top of the page
Nice to have
• Lots of room for pictures (e.g., see second page of this link:http://www.lumoraholdings.example/index.php?option=com_content&view=article&id=148:northbay-fuel-works-manufactured-mobile-homes&catid=44&Itemid=108 )

see also 2nd page: http://www.lumoraholdings.example/index.php?option=com_content&view=article&id=149:westridge-power-and-heat-manufactured-mobile-home-program&catid=44&Itemid=108

Front / back on 4 templates, color

```html
<!DOCTYPE html>
<html lang="en">
<head>
<meta charset="utf-8">
<title>Lumora Holdings – Tri-fold Inside Spread</title>
<link rel="stylesheet" href="https://fonts.googleapis.com/css2?family=Nunito+Sans:wght@300;400;700&display=swap">
<style>
  :root {
    --stage: #5f6a74;
    --navy-band: #0c2a66;
    --sky-top: #4260b8;
    --sky-mid: #5b7fd0;
    --sky-low: #8fa9e2;
    --sky-glow: #dfe8fb;
    --panel-white: #ffffff;
    --text-on-blue: #eef2fb;
    --text-dark: #333840;
    --heading-dark: #4a4f57;
    --label-blue: #2a8fd6;
    --label-on-blue: #9ec8f2;
    --quote-navy: #1b2f6e;
    --photo-warm: #8c7d6c;
    --photo-cool: #6f7c8c;
  }
  * { box-sizing: border-box; margin: 0; padding: 0; }
  html, body { width: 1200px; height: 900px; overflow: hidden; }
  body {
    background: var(--stage);
    font-family: "Nunito Sans", Arial, sans-serif;
    position: relative;
  }
  .spread {
    position: absolute; left: 80px; top: 48px; width: 1048px; height: 810px;
    background: var(--panel-white);
    overflow: hidden;
  }
  .spread__band {
    position: absolute; left: 0; top: 0; width: 100%; height: 30px;
    background: var(--navy-band);
  }
  .spread__sky {
    position: absolute; left: 0; top: 30px; width: 698px; height: 780px;
    background:
      radial-gradient(circle at 590px 590px, var(--sky-glow) 0, rgba(223,232,251,0.6) 70px, rgba(143,169,226,0) 230px),
      linear-gradient(180deg, var(--sky-top) 0%, var(--sky-mid) 45%, var(--sky-low) 100%);
  }
  .solar-array { position: absolute; left: 0; top: 472px; }

  .text-block { position: absolute; }
  .on-blue { color: var(--text-on-blue); }
  .on-white { color: var(--text-dark); }

  .panel-label { font-size: 13px; line-height: 16px; color: var(--label-on-blue); }
  .on-white .panel-label { color: var(--label-blue); }
  .panel-heading {
    font-weight: 300; font-size: 18.5px; line-height: 28px; text-transform: uppercase;
    margin-top: 4px; white-space: nowrap;
  }
  .on-white .panel-heading { color: var(--heading-dark); }

  .body-copy {
    font-size: 11.2px; line-height: 19.9px; text-align: justify;
    letter-spacing: -0.1px; hyphens: auto; -webkit-hyphens: auto;
  }
  .body-copy__lead { font-weight: 700; font-variant: small-caps; font-size: 12px; letter-spacing: 0; }

  .bullet-list { list-style: none; }
  .bullet-list li::before { content: "\25A0"; font-size: 9px; margin-right: 5px; vertical-align: 1px; }

  .photo { position: absolute; background: linear-gradient(135deg, var(--photo-cool), var(--photo-warm)); }
  .photo--framed { border: 2px solid #ffffff; }

  .pull-quote {
    position: absolute; left: 365px; top: 548px; width: 298px;
    font-size: 22px; line-height: 33px; color: var(--quote-navy); font-weight: 400;
  }
</style>
</head>
<body>
  <main class="spread">
    <div class="spread__sky"></div>
    <div class="spread__band"></div>

    <svg class="solar-array" width="400" height="338" viewBox="0 0 400 338" role="img" aria-label="Photo of a solar panel array against the sky">
      <defs>
        <linearGradient id="solarFill" x1="0" y1="0" x2="1" y2="1">
          <stop offset="0" stop-color="#2a4fc0"/>
          <stop offset="1" stop-color="#142b7a"/>
        </linearGradient>
      </defs>
      <polygon points="0,0 60,40 390,338 0,338" fill="url(#solarFill)"/>
    </svg>

    <!-- Left panel -->
    <header class="text-block on-blue" style="left:19px;top:52px;width:320px">
      <p class="panel-label">About Lumora Holdings</p>
      <h2 class="panel-heading">Norper augiam, vullutet,<br>sustrud delisim nullan prat.</h2>
    </header>
    <p class="text-block on-blue body-copy" style="left:19px;top:136px;width:313px"><span class="body-copy__lead">Lorem ipsum dolor sit amet,</span> consectetuer adipiscing elit, sed diam nonummy nibh euismod tincidunt ut laoreet dolore magna aliquam erat volutpat. Ut wisi enim ad minim veniam, quis nostrud exerci tation ullamcorper suscipit lobortis nisl ut aliquip ex ea commodo consequat. Duis autem vel eum iriure dolor in hendrerit in vulputate velit esse molestie consequat, vel illum dolore eu feugiat nulla facilisis at vero.</p>
    <ul class="text-block on-blue body-copy bullet-list" style="left:19px;top:294px;width:313px">
      <li>Api non habent claritatem insitam; est usus legentis inis qui facit eorum claritatem. Investigationes demonstrave.</li>
      <li>Ectores legere me lius quod ii legunt saepius.</li>
      <li>Claritas est etiam processus dynamicus, qui sequitur mutationem consuetudium lectorum.</li>
      <li>Mirum est notare quam littera gothica, quam putamus</li>
      <li>Anteposuerit litterarum formas humanitatis per seacula quarta decima et quinta decima. Eodem modo typi</li>
      <li>Nobis videntur parum clari, fiant sollemnes in futurum</li>
    </ul>

    <!-- Middle panel -->
    <header class="text-block on-blue" style="left:367px;top:52px;width:320px">
      <p class="panel-label">About Lumora Holdings</p>
      <h2 class="panel-heading">Norper augiam, vullutet,<br>sustrud delisim nullan prat</h2>
    </header>
    <div class="photo photo--framed" style="left:367px;top:142px;width:154px;height:98px" role="img" aria-label="Photo of a technician servicing a rooftop unit"></div>
    <div class="photo photo--framed" style="left:530px;top:142px;width:154px;height:98px" role="img" aria-label="Photo of a technician servicing a rooftop unit"></div>
    <p class="text-block on-blue body-copy" style="left:367px;top:264px;width:318px"><span class="body-copy__lead">Lorem ipsum dolor sit amet,</span> consectetuer adipiscing elit, sed diam nonummy nibh euismod tincidunt ut laoreet dolore magna aliquam erat volutpat. Ut wisi enim ad minim veniam, quis nostrud exerci tation ullamcorper suscipit lobortis nisl ut aliquip ex ea commodo consequat. Duis autem vel eum iriure dolor in hendrerit in vulputate velit esse molestie consequat, vel illum dolore eu feugiat nulla facilisis at vero eros</p>
    <p class="text-block on-blue body-copy" style="left:367px;top:423px;width:318px">Typi non habent claritatem insitam; est usus legentis in iis qui facit eorum claritatem. Investigationes demonstraverunt lectores legere me lius quod ii legunt saepius. Claritas est etiam processus dynamicus, qui sequitur mutationem .</p>
    <p class="pull-quote">Dolor ipit la feu accum iure dunt praesequat, sumsan hendipit inciliq. Ore esent non veniat, quismodo autat mincidunt utpatet la iritus</p>

    <!-- Right panel -->
    <header class="text-block on-white" style="left:717px;top:52px;width:320px">
      <p class="panel-label">About Lumora Holdings</p>
      <h2 class="panel-heading">Norper augiam, vullutet,<br>sustrud delisim nullan prat.</h2>
    </header>
    <p class="text-block on-white body-copy" style="left:717px;top:136px;width:317px"><span class="body-copy__lead">Lorem ipsum dolor sit amet,</span> consectetuer adipiscing elit, sed diam nonummy nibh euismod tincidunt ut laoreet dolore magna aliquam erat volutpat. Ut wisi enim ad minim veniam, quis nostrud exerci tation ullamcorper suscipit lobortis nisl ut aliquip ex ea commodo consequat. Duis autem vel eum iriure dolor in hendrerit in vulputate velit esse molestie.</p>
    <div class="photo" style="left:698px;top:272px;width:227px;height:133px" role="img" aria-label="Photo of attic ductwork and insulation equipment"></div>
    <div class="photo" style="left:936px;top:272px;width:112px;height:133px" role="img" aria-label="Photo of a technician sealing a floor vent"></div>
    <p class="text-block on-white body-copy" style="left:717px;top:434px;width:317px">Typi non habent claritatem insitam; est usus legentis in iis qui facit eorum claritatem. Investigationes demonstraverunt lectores legere me lius quod ii legunt saepius. Claritas est etiam processus dynamicus, qui sequitur mutationem consuetudium lectorum. Mirum est notare quam littera gothica, quam nunc putamus parum claram, anteposuerit litterarum formas humanitatis per seacula quarta decima et quinta decima. Eodem modo typi, qui nunc nobis videntur parum clari, fiant sollemnes in futurum.</p>
    <div class="photo" style="left:719px;top:623px;width:150px;height:95px" role="img" aria-label="Photo of a technician servicing a rooftop unit"></div>
    <div class="photo" style="left:882px;top:623px;width:150px;height:95px" role="img" aria-label="Photo of a technician servicing a rooftop unit"></div>
  </main>
</body>
</html>
```